Lanternfield Voyages Business Card Design for Home Based Travel Agency

We already have a logo and I would like to see about getting a Business Card Design. The font on the logo can be changed. We are a home based travel agency and sell cruises and tour packages, etc. I would like the following information put into the design Name of Company and Tag Line from the logo. I would also like the email info@lanternfieldvoyages.example Phone 555-238-6140. Website www.lanternfieldvoyages.example. My name Neil Parton Travel Consultant and my wife's Name Mavis Parton. I would like you to use your imagination as nothing is off limites. Impress Me!

Target Market(s)

Baby Boomers

Industry/Entity Type

Travel Agent

Contact Information for Business Card

See above

Font styles to use
Serif
Sans Serif

Colors

Designer to choose colors to be used in the design.

Requirements
Must have
• Play with different fonts and needs to be easily readable, i.e. not too small of print.
Nice to have
• Use your imagination

```html
<!DOCTYPE html>
<html lang="en">
<head>
<meta charset="utf-8">
<title>Lanternfield Voyages – Business Card</title>
<link rel="stylesheet" href="https://fonts.googleapis.com/css2?family=Marcellus&family=Roboto+Condensed:wght@300;400&display=swap">
<style>
  :root {
    --navy: #0d2a78;
    --royal: #0b4fa8;
    --cyan: #00aeef;
    --orange: #f7941d;
    --orange-red: #f05a28;
    --white: #ffffff;
    --ink: #111111;
    --icon-ink: #3b1f4a;
    --backdrop: #ebe8e4;
  }
  * { margin: 0; padding: 0; box-sizing: border-box; }
  html, body {
    width: 1200px; height: 1200px; overflow: hidden;
    background: var(--backdrop);
  }
  .card {
    position: absolute;
    left: 237px;
    width: 743px;
    height: 422px;
    overflow: hidden;
    box-shadow: 0 6px 18px rgba(0,0,0,0.18);
  }
  .card--front { top: 120px; }
  .card--back { top: 633px; height: 412px; }
  .card__art { position: absolute; inset: 0; width: 100%; height: 100%; }

  .brand {
    position: absolute; left: 0; right: 0; top: 268px;
    text-align: center;
    font-family: "Marcellus", serif;
    font-size: 46px;
    color: var(--ink);
    letter-spacing: 1px;
  }
  .tagline {
    position: absolute; left: 0; right: 0; top: 336px;
    text-align: center;
    font-family: "Roboto Condensed", sans-serif;
    font-weight: 300;
    font-size: 19px;
    color: #333333;
  }

  .people {
    position: absolute; left: 0; right: 0; top: 74px;
    text-align: center;
  }
  .people__name {
    display: block;
    font-family: "Marcellus", serif;
    font-size: 29px;
    line-height: 32px;
    color: var(--ink);
  }
  .people__rule {
    width: 195px; height: 2px; margin: 2px auto 4px;
    background: var(--ink);
  }
  .people__role {
    display: block;
    font-family: "Roboto Condensed", sans-serif;
    font-size: 21px;
    color: var(--ink);
  }

  .contact {
    position: absolute;
    display: flex; align-items: center; gap: 18px;
    font-family: "Roboto Condensed", sans-serif;
    font-size: 23px;
    color: var(--white);
    white-space: nowrap;
  }
  .contact__icon { width: 50px; height: 56px; flex: none; }
  .contact--web { left: 40px; top: 271px; }
  .contact--phone { left: 481px; top: 271px; }
  .contact--mail { left: 171px; top: 330px; }
</style>
</head>
<body>

<section class="card card--front" aria-label="Card front">
  <svg class="card__art" viewBox="0 0 929 527" preserveAspectRatio="none" aria-hidden="true">
    <defs>
      <linearGradient id="blueSheen" x1="0" y1="0" x2="1" y2="0">
        <stop offset="0" stop-color="#0d2a78"/>
        <stop offset="0.3" stop-color="#0b4fa8"/>
        <stop offset="0.5" stop-color="#00aeef"/>
        <stop offset="0.7" stop-color="#0b4fa8"/>
        <stop offset="1" stop-color="#0d2a78"/>
      </linearGradient>
    </defs>
    <rect width="929" height="527" fill="url(#blueSheen)"/>
    <path d="M0,205 Q464,35 929,210 L929,527 L0,527 Z" fill="var(--orange)"/>
    <path d="M0,290 Q464,-55 929,295 L929,527 L0,527 Z" fill="var(--orange-red)"/>
    <path d="M0,318 Q464,-72 929,322 L929,527 L0,527 Z" fill="var(--white)"/>
  </svg>
  <div class="brand">Lanternfield Voyages</div>
  <div class="tagline">Every Journey Becomes a Tale to Remember</div>
</section>

<section class="card card--back" aria-label="Card back">
  <svg class="card__art" viewBox="0 0 929 515" preserveAspectRatio="none" aria-hidden="true">
    <defs>
      <linearGradient id="blueSheenBack" x1="0" y1="0" x2="1" y2="0">
        <stop offset="0" stop-color="#0d2a78"/>
        <stop offset="0.3" stop-color="#0b4fa8"/>
        <stop offset="0.5" stop-color="#00aeef"/>
        <stop offset="0.7" stop-color="#0b4fa8"/>
        <stop offset="1" stop-color="#0d2a78"/>
      </linearGradient>
    </defs>
    <rect width="929" height="515" fill="var(--white)"/>
    <path d="M0,135 Q464,432 929,128 L929,515 L0,515 Z" fill="var(--orange-red)"/>
    <path d="M0,158 Q464,410 929,152 L929,515 L0,515 Z" fill="var(--orange)"/>
    <path d="M0,220 Q464,350 929,215 L929,515 L0,515 Z" fill="url(#blueSheenBack)"/>
  </svg>

  <div class="people">
    <span class="people__name">Neil Parton</span>
    <span class="people__name">Mavis Parton</span>
    <div class="people__rule"></div>
    <span class="people__role">Travel Consultant</span>
  </div>

  <div class="contact contact--web">
    <svg class="contact__icon" viewBox="0 0 50 56" aria-hidden="true">
      <path d="M25,1 L49,15 L49,41 L25,55 L1,41 L1,15 Z" fill="var(--orange)"/>
      <g fill="none" stroke="var(--icon-ink)" stroke-width="3" stroke-linecap="round">
        <rect x="12" y="26" width="16" height="9" rx="4.5" transform="rotate(-45 20 30.5)"/>
        <rect x="22" y="21" width="16" height="9" rx="4.5" transform="rotate(-45 30 25.5)"/>
      </g>
    </svg>
    <span>www.lanternfieldvoyages.example</span>
  </div>

  <div class="contact contact--phone">
    <svg class="contact__icon" viewBox="0 0 50 56" aria-hidden="true">
      <path d="M25,1 L49,15 L49,41 L25,55 L1,41 L1,15 Z" fill="var(--orange)"/>
      <path d="M18,16 L22,16 L24,22 L21,24 Q23,31 29,35 L31,32 L37,34 L37,38 Q34,42 29,40 Q18,34 15,22 Q14,17 18,16 Z" fill="var(--icon-ink)"/>
    </svg>
    <span>(555) 238 6140</span>
  </div>

  <div class="contact contact--mail">
    <svg class="contact__icon" viewBox="0 0 50 56" aria-hidden="true">
      <path d="M25,1 L49,15 L49,41 L25,55 L1,41 L1,15 Z" fill="var(--orange)"/>
      <g fill="none" stroke="var(--icon-ink)" stroke-width="2.6" stroke-linejoin="round">
        <rect x="12" y="19" width="26" height="18" rx="2"/>
        <path d="M12,19 L25,30 L38,19 M12,37 L21,27 M38,37 L29,27"/>
      </g>
    </svg>
    <span>info@lanternfieldvoyages.example</span>
  </div>
</section>

</body>
</html>
```